Flyer Design Project

I am opening a yoga studio called Willowmere Yoga .Pilates. Fitness
and require a flyer that will be letterbox dropped. It will two sided - DL size.100mm × 210mm

The studio will offer Vinyasa Flow Yoga and Mat Pilates classes. We aim to enable people to lead healthier, happier lives through improved strength, flexibility and general well being that regular yoga and pilates practice offers.

We offer group classes, private and semi private sessions in yoga and pilates.

it must have the logo on it- I have uploaded the logo in two versions - not sure what will look the best.

pick up one of the colours from the logo as the background colour.

Side one:
Simple and clean with one side showing logo and address details, website and with simple intro about studio (if it fits)

Location: 1st Floor, 17 Larkspur Parade, Tindale, 3286
phone: 0428 596143
www.willowmeretindale.com.au

OPENING OCTOBER

other side - class descriptions and intro offer for new clients
$20 for 7 days of classes
$99 for 1 month unlimited.

Class descriptions:
Vinyasa Flow yoga: A class that flows from pose to pose integrating breath, alignment, strength and power. All levels are catered for in a warm room heated to around 26 degrees. You will leave feeling inspired, empowered and energised.

Mat Pilates: A strong, challenging class integrating the key principles of pilates: concentration, control, centring, precision, flowing movement and breath. Using the core as a focus to develop these principles you will be hooked on the physical freedom you experience post workout:improved strength, flexibility and vitality that pilates offers.

Private and semi Private tuition available.

Target Market(s)

mainly women, athletic, 35-55 age, middle class, well educated

Industry/Entity Type

Fitness

Requirements
Must have
• 2 pages
the logo

Should not have
• no pics

```html
<!DOCTYPE html>
<html lang="en">
<head>
<meta charset="utf-8">
<title>Willowmere Yoga .Pilates. Fitness – Flyer</title>
<link rel="stylesheet" href="https://fonts.googleapis.com/css2?family=Arimo&family=Montserrat:wght@600&family=Merienda:wght@400&display=swap">
<style>
  :root {
    --frame: #000000;
    --sky: #4fd0f5;
    --sky-light: #8fe6fb;
    --sun-top: #f8e43c;
    --sun-mid: #e79a17;
    --sun-bottom: #f6dc2e;
    --mark: #f29a1c;
    --name: #5e5e5e;
    --tagline: #6a4a18;
    --ink: #111111;
  }
  html, body {
    margin: 0;
    padding: 0;
    width: 1200px;
    height: 2522px;
    overflow: hidden;
    background: var(--frame);
  }
  .flyer {
    position: relative;
    width: 1200px;
    height: 2522px;
    background: var(--frame);
  }
  .panel {
    position: absolute;
    left: 42px;
    top: 42px;
    width: 1116px;
    height: 2438px;
    overflow: hidden;
    background: linear-gradient(180deg, var(--sun-top) 0%, var(--sun-top) 14%, var(--sun-mid) 62%, var(--sun-bottom) 100%);
    box-shadow: inset 0 0 40px rgba(0,0,0,0.45);
  }
  .sky-wave {
    position: absolute;
    left: 0;
    top: 0;
    width: 1116px;
    height: 460px;
  }
  .brand {
    position: absolute;
    left: 0;
    top: 700px;
    width: 1116px;
    text-align: center;
  }
  .brand-dot {
    display: block;
    width: 380px;
    height: 380px;
    margin: 0 auto 60px;
    border-radius: 50%;
    background: var(--mark);
  }
  .brand-name {
    margin: 0;
    font-family: "Montserrat", sans-serif;
    font-weight: 600;
    color: var(--name);
    font-size: 84px;
    line-height: 1.1;
    letter-spacing: 2px;
  }
  .brand-name span { display: block; font-size: 60px; letter-spacing: 10px; }
  .tagline {
    position: absolute;
    left: 0;
    top: 1420px;
    width: 1116px;
    margin: 0;
    text-align: center;
    font-family: "Merienda", cursive;
    font-size: 36px;
    color: var(--tagline);
  }
  .contact {
    position: absolute;
    left: 42px;
    top: 1860px;
    width: 1032px;
    font-family: "Arimo", Arial, sans-serif;
    font-size: 44px;
    line-height: 54px;
    color: var(--ink);
    word-spacing: 10px;
    letter-spacing: 1px;
  }
  .contact p { margin: 0 0 54px; }
  .address { text-align: justify; text-align-last: left; }
  .website {
    color: var(--ink);
    text-decoration: underline;
    text-underline-offset: 8px;
    text-decoration-thickness: 2px;
  }
</style>
</head>
<body>
<main class="flyer">
  <section class="panel">
    <svg class="sky-wave" viewBox="0 0 1116 460" aria-hidden="true">
      <defs>
        <linearGradient id="skyFill" x1="0" y1="0" x2="0" y2="1">
          <stop offset="0" stop-color="var(--sky)"/>
          <stop offset="1" stop-color="var(--sky-light)"/>
        </linearGradient>
        <filter id="waveShadow" x="-5%" y="-5%" width="110%" height="130%">
          <feDropShadow dx="0" dy="10" stdDeviation="12" flood-color="#6a4a00" flood-opacity="0.45"/>
        </filter>
      </defs>
      <path d="M0 0 H1116 V380 C1000 410 900 360 760 330 C600 295 470 360 320 400 C180 435 80 390 0 340 Z"
            fill="url(#skyFill)" filter="url(#waveShadow)"/>
    </svg>

    <div class="brand">
      <span class="brand-dot"></span>
      <h1 class="brand-name">Willowmere Yoga<span>.Pilates. Fitness</span></h1>
    </div>

    <p class="tagline">Strength. Flexibility. Wellness.</p>

    <div class="contact">
      <p class="address">Address: 1st Floor, 17 Larkspur Parade, Tindale, 3286</p>
      <p>Phone: 0428 596143<br>Opening Hours (7am - 9pm)</p>
      <p>Visit us at:<br><span class="website">www.willowmeretindale.com.au</span></p>
    </div>
  </section>
</main>
</body>
</html>
```